Brightstone Roofing Business Card

This is my current business card. But I’d like to make some changes. Somewhere on the card I’d like to list some of the services we offer. Maybe on the back? But I’d still like to keep the red. White and black modern look.

-residential & commercial roofing
-Roof Repairs & Maintenance
-Storm Damage & Insurance Claims specialist
-Christmas Lights and permanent Christmas lights
Fencing. Windows. Gutters. Siding. Sheetrock, painting.

```html
<!DOCTYPE html>
<html lang="en">
<head>
<meta charset="utf-8">
<title>Brightstone Roofing Business Card</title>
<link href="https://fonts.googleapis.com/css2?family=Michroma&family=Montserrat:wght@400;500;600;700&display=swap" rel="stylesheet">
<style>
  :root {
    --stage: #b9b9b9;
    --red: #e3131b;
    --ink: #111111;
    --paper: #f6f6f6;
    --paper-shade: #e9e9e9;
    --night: #0c0c0c;
    --night-shade: #1a1a1a;
    --light-text: #f2f2f2;
  }
  * { box-sizing: border-box; margin: 0; padding: 0; }
  html, body { width: 1200px; height: 1015px; overflow: hidden; }
  body {
    background: var(--stage);
    font-family: "Montserrat", sans-serif;
    position: relative;
  }
  .card {
    position: absolute;
    left: 220px;
    width: 760px;
    height: 434px;
    overflow: hidden;
    box-shadow: 0 14px 30px rgba(0,0,0,0.35);
  }
  .card-back { top: 50px; background: var(--night); }
  .card-front { top: 531px; background: var(--paper); }
  .surface { position: absolute; inset: 0; }
  .card-back .surface { background: linear-gradient(160deg, var(--night-shade) 0%, var(--night) 100%); }
  .card-front .surface { background: linear-gradient(160deg, var(--paper) 0%, var(--paper-shade) 100%); }

  /* back: services */
  .services {
    position: absolute; inset: 0;
    display: flex; flex-direction: column; align-items: center; justify-content: center;
    color: var(--light-text); text-align: center;
  }
  .service-list { list-style: none; font-size: 22px; font-weight: 500; line-height: 1.55; }
  .services-rule { width: 520px; height: 1px; background: var(--red); margin: 24px 0 20px; }
  .trade-list {
    list-style: none; display: flex; gap: 10px; font-size: 18px; font-weight: 500; letter-spacing: 0.3px;
  }
  .trade-list li + li::before { content: "•"; color: var(--red); margin-right: 10px; }

  /* front: brand + contact */
  .brand {
    position: absolute; left: 60px; top: 0; height: 100%; width: 300px;
    display: flex; flex-direction: column; align-items: center; justify-content: center; gap: 22px;
  }
  .brand-mark { width: 150px; height: 150px; border-radius: 50%; background: var(--red); }
  .brand-name {
    font-family: "Montserrat", sans-serif; font-weight: 700; color: var(--red);
    font-size: 30px; line-height: 1.15; text-align: center; letter-spacing: 1px; text-transform: uppercase;
  }
  .divider { position: absolute; left: 385px; top: 95px; width: 1px; height: 245px; background: var(--red); }
  .contact { position: absolute; left: 420px; top: 100px; color: var(--ink); }
  .person-name { font-family: "Michroma", sans-serif; font-size: 27px; letter-spacing: 0.5px; line-height: 1; font-weight: 400; }
  .person-name .first { color: var(--red); }
  .person-role { font-size: 22px; font-weight: 500; margin-top: 8px; letter-spacing: 0.5px; }
  .contact-list { list-style: none; margin-top: 30px; display: flex; flex-direction: column; gap: 12px; }
  .contact-list li { display: flex; align-items: center; gap: 10px; font-size: 19px; font-weight: 500; }
  .icon {
    width: 28px; height: 28px; border-radius: 50%; background: var(--red);
    display: flex; align-items: center; justify-content: center; flex: none;
  }
  .icon svg { width: 16px; height: 16px; }
</style>
</head>
<body>

<section class="card card-back">
  <div class="surface" role="img" aria-label="Dark metal roofing texture background"></div>
  <div class="services">
    <ul class="service-list">
      <li>Residential &amp; Commercial Roofing</li>
      <li>Roof Repairs &amp; Maintenance</li>
      <li>Storm Damage &amp; Insurance Claims Specialist</li>
      <li>Christmas Lights and Permanent Christmas Lights</li>
    </ul>
    <div class="services-rule"></div>
    <ul class="trade-list">
      <li>FENCING</li><li>WINDOWS</li><li>GUTTERS</li><li>SIDING</li><li>SHEETROCK</li><li>PAINTING.</li>
    </ul>
  </div>
</section>

<section class="card card-front">
  <div class="surface" role="img" aria-label="Light metal roofing texture background"></div>
  <div class="brand">
    <div class="brand-mark"></div>
    <div class="brand-name">Brightstone<br>Roofing Co.</div>
  </div>
  <div class="divider"></div>
  <div class="contact">
    <h1 class="person-name"><span class="first">DEAN</span> MERCER</h1>
    <p class="person-role">OWNER</p>
    <ul class="contact-list">
      <li>
        <span class="icon"><svg viewBox="0 0 16 16"><path d="M4 2l2.5 3-1.5 1.5a8 8 0 0 0 4.5 4.5L11 9.5l3 2.5-1.5 2.5C7 14 2 9 1.5 3.5z" fill="#fff"/></svg></span>
        555-014-2238
      </li>
      <li>
        <span class="icon"><svg viewBox="0 0 16 16"><rect x="2" y="4" width="12" height="8" fill="#fff"/><path d="M2 4l6 5 6-5" fill="none" stroke="#e3131b" stroke-width="1.2"/></svg></span>
        dean@brightstoneroofing.co
      </li>
      <li>
        <span class="icon"><svg viewBox="0 0 16 16"><circle cx="8" cy="8" r="6" fill="none" stroke="#fff" stroke-width="1.3"/><ellipse cx="8" cy="8" rx="2.6" ry="6" fill="none" stroke="#fff" stroke-width="1.1"/><path d="M2 8h12" stroke="#fff" stroke-width="1.1"/></svg></span>
        www.brightstoneroofing.co
      </li>
    </ul>
  </div>
</section>

</body>
</html>
```